Australian Trucking Company Requires Professional Looking Stationary

We require a professional looking stationary design that incorporates our newly designed logo.

Our business, called "Vell Haulage Contracting", provides contracting work, transport and logistics to business in Western Australia particularly with links to the mining sector.

We are a small business looking to expand and our new logo and our new stationary will help develop our brand image in our market place.

Target Market(s)

Businesses and Corporation with links to the Mining Sector

Industry/Entity Type

Small Business

Requirements
Must have
• The letterhead must have the following details:
The new logo

Text saying: "Vell Haulage Pty Ltd (ACN 582 306 917) ATF The Vell Discretionary Trust T/AS"
"ABN 71 840 295 613"
Address "P.O Box 718 Norbrook WA, 6043"
Phone: 08 9275 4180
Email: vellhaul@maillane.com.au

The text on the letterhead should be editable as the details are likely to change in the near future. Provision should be made for a website address all though one isn't available at the moment.

The styling, layout and font text is entirely up to the designer.

```html
<!DOCTYPE html>
<html lang="en">
<head>
<meta charset="utf-8">
<title>Vell Haulage Contracting – Stationery Set</title>
<link href="https://fonts.googleapis.com/css2?family=Arimo:ital,wght@0,400;0,700;1,700&family=Tinos&display=swap" rel="stylesheet">
<style>
  :root {
    --brand-red: #8e2a2f;
    --logo-red: #b3262d;
    --ink: #444444;
    --ink-soft: #8a8a8a;
    --paper: #ffffff;
    --backdrop-light: #fbfbfb;
    --backdrop-dark: #d9d9d9;
    --rule: #3a3a3a;
    --hole: #e6e6e6;
    --decor: rgba(190, 190, 190, 0.35);
  }
  html, body {
    margin: 0;
    padding: 0;
    overflow: hidden;
  }
  body {
    width: 1200px;
    height: 895px;
    position: relative;
    background: radial-gradient(ellipse at 55% 40%, var(--backdrop-light) 0%, #eeeeee 55%, var(--backdrop-dark) 100%);
    font-family: "Arimo", Arial, sans-serif;
    color: var(--ink);
  }
  .piece {
    position: absolute;
    background: var(--paper);
    box-shadow: 0 2px 6px rgba(0, 0, 0, 0.18);
    overflow: hidden;
  }
  .decor {
    position: absolute;
    background: linear-gradient(135deg, rgba(255,255,255,0) 0%, var(--decor) 60%, rgba(220,220,220,0.5) 100%);
  }
  .logo {
    position: absolute;
    display: flex;
    align-items: center;
    gap: 10px;
  }
  .logo-mark {
    width: 30px;
    height: 30px;
    background: var(--ink);
    flex: none;
  }
  .logo-name {
    font-weight: 700;
    color: var(--logo-red);
    text-transform: uppercase;
    line-height: 0.98;
    letter-spacing: 0.5px;
    margin: 0;
  }

  /* Business card – front */
  .card-front { left: 38px; top: 60px; width: 311px; height: 170px; border-radius: 10px; }
  .card-front .logo { left: 62px; top: 56px; }
  .card-front .logo-mark { width: 36px; height: 36px; }
  .card-front .logo-name { font-size: 17px; }
  .card-legal {
    position: absolute; left: 15px; bottom: 4px; margin: 0;
    font-size: 6.3px; color: var(--ink); white-space: nowrap;
    display: flex; gap: 14px;
  }

  /* Business card – back */
  .card-back { left: 416px; top: 64px; width: 311px; height: 171px; border-radius: 10px; }
  .card-back .decor { right: 0; top: 0; width: 140px; height: 171px; }
  .name-tag {
    position: absolute; left: 0; top: 24px; width: 134px; height: 30px;
    background: var(--brand-red);
    clip-path: polygon(0 0, 100% 0, 92% 100%, 0 100%);
    color: var(--paper);
  }
  .name-tag .person { position: absolute; left: 11px; top: 6px; margin: 0; font-size: 10.5px; font-weight: 700; font-style: italic; letter-spacing: 0.4px; white-space: nowrap; }
  .name-tag .role { position: absolute; left: 42px; top: 20px; margin: 0; font-size: 4.5px; font-weight: 700; letter-spacing: 0.3px; white-space: nowrap; }
  .card-address { position: absolute; left: 12px; top: 120px; margin: 0; font-size: 9px; line-height: 11px; color: var(--ink); font-style: normal; }
  .card-contacts { position: absolute; left: 122px; top: 85px; margin: 0; padding: 0; list-style: none; font-size: 8.3px; line-height: 10.2px; color: var(--ink); }

  /* Disc label */
  .disc { left: 795px; top: 170px; width: 370px; height: 370px; border-radius: 50%; }
  .disc .decor { left: 190px; top: 60px; width: 180px; height: 300px; }
  .disc .logo { left: 82px; top: 42px; }
  .disc .logo-mark { width: 34px; height: 34px; }
  .disc .logo-name { font-size: 16px; }
  .disc-hole { position: absolute; left: 152px; top: 134px; width: 66px; height: 66px; border-radius: 50%; background: var(--hole); box-shadow: inset 0 1px 3px rgba(0,0,0,0.15); }
  .disc-band {
    position: absolute; left: 0; top: 270px; width: 241px; height: 33px;
    background: var(--brand-red);
    clip-path: polygon(0 0, 100% 0, 91% 100%, 0 100%);
  }
  .disc-topic { position: absolute; left: 71px; top: 277px; margin: 0; font-size: 17px; color: var(--paper); white-space: nowrap; }

  /* Letterhead */
  .letterhead { left: 66px; top: 342px; width: 362px; height: 471px; }
  .letterhead .decor { right: 0; bottom: 0; width: 135px; height: 125px; }
  .letterhead .logo { left: 98px; top: 24px; }
  .letterhead .logo-mark { width: 34px; height: 34px; }
  .letterhead .logo-name { font-size: 13px; }
  .letter-rule { position: absolute; left: 0; top: 84px; width: 100%; height: 1px; background: var(--rule); }
  .letter-date { position: absolute; left: 290px; top: 106px; margin: 0; font-family: "Tinos", "Times New Roman", serif; font-size: 11px; color: var(--ink-soft); }
  .letter-body { position: absolute; left: 50px; top: 130px; width: 250px; font-size: 5.6px; line-height: 7.4px; color: var(--ink-soft); }
  .letter-body p { margin: 0 0 7px; }

  /* Shared footer: band drawn behind, text never clipped */
  .stationery-footer {
    position: absolute; left: 0; bottom: 0;
    color: var(--paper);
  }
  .stationery-footer::before {
    content: "";
    position: absolute; inset: 0;
    background: var(--brand-red);
    clip-path: polygon(0 0, 100% 0, 94% 100%, 0 100%);
  }
  .footer-text { position: relative; margin: 0; font-style: normal; white-space: nowrap; }

  .letterhead .stationery-footer { width: 258px; height: 26px; }
  .letterhead .footer-text { padding: 1px 0 0 12px; font-size: 5.6px; line-height: 8px; }

  /* Envelope */
  .envelope { left: 498px; top: 583px; width: 412px; height: 220px; border-radius: 15px 15px 0 0; }
  .envelope .decor { right: 0; bottom: 0; width: 125px; height: 115px; }
  .envelope-flap { position: absolute; left: 0; top: 0; width: 100%; height: 45px; background: var(--brand-red); }
  .envelope-seam { position: absolute; left: 0; top: 45px; width: 100%; height: 8px; background: linear-gradient(to right, #222 0%, #6a6a6a 50%, #222 100%); }
  .envelope .stationery-footer { width: 324px; height: 32px; }
  .envelope .footer-text { padding: 1px 0 0 14px; font-size: 6.9px; line-height: 10px; }
</style>
</head>
<body>

  <section class="piece card-front" aria-label="Business card front">
    <div class="logo">
      <span class="logo-mark"></span>
      <p class="logo-name">Vell<br>Haulage<br>Contracting</p>
    </div>
    <p class="card-legal">
      <span>ABN 71 840 295 613</span>
      <span>Vell Haulage Pty Ltd (ACN 582 306 917) ATF The Vell Discretionary Trust T/AS</span>
    </p>
  </section>

  <section class="piece card-back" aria-label="Business card back">
    <div class="decor" role="img" aria-label="Faint large truck illustration"></div>
    <div class="name-tag">
      <p class="person">MARLO TRENNICK</p>
      <p class="role">MANAGING DIRECTOR</p>
    </div>
    <address class="card-address">P.O Box 718 Norbrook<br>WA, 6043</address>
    <ul class="card-contacts">
      <li>P: 08 9275 4180</li>
      <li>F: 770-418-5092</li>
      <li>E: vellhaul@maillane.com.au</li>
      <li>W: www.vellhaul.com.au</li>
    </ul>
  </section>

  <section class="piece disc" aria-label="Disc label">
    <div class="decor" role="img" aria-label="Faint large truck illustration"></div>
    <div class="logo">
      <span class="logo-mark"></span>
      <p class="logo-name">Vell<br>Haulage<br>Contracting</p>
    </div>
    <div class="disc-hole"></div>
    <div class="disc-band"></div>
    <p class="disc-topic">Topic Name Here</p>
  </section>

  <section class="piece letterhead" aria-label="Letterhead">
    <div class="decor" role="img" aria-label="Faint large truck illustration"></div>
    <div class="logo">
      <span class="logo-mark"></span>
      <p class="logo-name">Vell<br>Haulage<br>Contracting</p>
    </div>
    <div class="letter-rule"></div>
    <p class="letter-date">Date:_____</p>
    <div class="letter-body">
      <p>Hello There,</p>
      <p>Thank you for your recent enquiry about our haulage services. We provide reliable transport and logistics across Western Australia, with a strong focus on the mining sector. Our fleet is maintained to a high standard and our drivers are fully accredited for site work.</p>
      <p>We understand that deadlines on remote projects leave little room for delay. Each job is planned in advance, tracked on the road and confirmed on delivery, so you always know where your freight is and when it will arrive.</p>
      <p>Our team can supply equipment, plant and general contracting support for short and long term works. Please find our rates attached for your review, along with a summary of the services we can offer to your business.</p>
      <p>Should you have any questions, please contact our office and we will be glad to help.</p>
      <p>Best Regards,</p>
    </div>
    <div class="stationery-footer">
      <address class="footer-text">P.O Box 718 Norbrook<br>WA, 6043<br>P: 08 9275 4180 &nbsp;F: 770-418-5092 &nbsp;E: vellhaul@maillane.com.au &nbsp;W: www.vellhaul.com.au</address>
    </div>
  </section>

  <section class="piece envelope" aria-label="Envelope">
    <div class="decor" role="img" aria-label="Faint large truck illustration"></div>
    <div class="envelope-flap"></div>
    <div class="envelope-seam"></div>
    <div class="stationery-footer">
      <address class="footer-text">P.O Box 718 Norbrook<br>WA, 6043<br>P: 08 9275 4180 &nbsp;F: 770-418-5092 &nbsp;E: vellhaul@maillane.com.au &nbsp;W: www.vellhaul.com.au</address>
    </div>
  </section>

</body>
</html>
```